Flyer Design - High Quality

*** Although this current job contest is listed as a ‘one-off contest’ we are also looking at working with a graphic designer long-term, which will include quite regular design work. So even though this is just a small job, if you want to & you do a good job on this, we would love to look at working with you on a regular basis.
* The winning designer will also get a freelance job designing another flyer in same design
Job Basics:
1. the design of a ….
Promotional corporate flyer - size = A4 - approx 6 or 7 pages.
*** The design will need to be extremely high quality/professional. Must be of a similar or better standard as the attached flyers – 1) Ross Penley_Info Pack & 2) DrGlen Whitcombe
* Please view these flyers first to ensure you can create a flyer of similar or better quality before proceeding.
Specific Requirements:
1. high-quality, professional promotional flyer [size = A4 - for online use predominantly . I.e. not for printing necessarily] using the text, images and basic instructions outlined on the word document attached - 'Flyer_All talks in 1_guidelines'.
2. Examples of similar quality (good) designs = 1) Ross Penley_Info Pack & 2) DrGlen Whitcombe
Background:
I am a motivational speaker on health, well-being and work-life balance. This flyer is to be used for promotional purposes when clients inquire about me speaking at their conference. Ross Penley & Glen Whitcombe are speakers who do somewhat similar talks to me, and who have flyers that I really like.
Theme: My general theme is ‘health and well-being’ (we're a little bit more towards natural health and Eastern medicine, but don't want it too ‘eastern’ if you know what I mean).
Main Look & Feel … to be conveyed:
Professional / Corporate
Health, Vitality and happiness (fresh, modern and vital)
eye-catching / attention grabbing
* The design should represent a balance between highly sophisticated, professional and classy - corporate savvy - with a hint of 'natural health, Eastern wisdom and a general ‘high energy/fresh health and vitality feel'. While we would like the design to convey some aspect of ‘ natural/Eastern’ wisdom), we predominantly want to convey the idea of ‘modern’ health (i.e. fresh, modern and vital).
Colours:
We are open to your creative suggestions, but were generally thinking something along the lines of the colours in our corporate logo –
dark blue, aqua blue, grey – see logo (KVT_300kb.jpg) in attachments
- possibly with some bright green, orange etc if you think it might suit – to help give it the ‘natural health’ feel.
* Notes:
1. SAVING YOUR TIME: If you just want to start just doing a quickish design of the first 1-2 pages and submitting that (images for these pages attached - though use own images if you think they are better), then that’s fine. Then we can let you know if it is along the lines of something we like or not. This way, you can do something relatively quickly, without wasting too much time, if it is definitely not something we like. Hope that helps - we are always conscious of trying to make things good for you as a designer too.
2. Do not feel completely bound to the ideas suggested/asked for. Feel free to convey the basic ideas/keys but feel free to use/follow some of your own ideas/creative desires.
3. Any photos/images should be royalty free (or ask us if we want to pay for it) and not widely used or seen in the public domain - i.e. we don’t want people to have seen the photo/image elsewhere (within reason).
Thanks a lot and look forward to receiving your first design!
Cheers
Owen
Target Market(s)
Predominantly corporates / business groups.
Industry/Entity Type
Graphic Designer

```html
<!DOCTYPE html>
<html lang="en">
<head>
<meta charset="utf-8">
<title>Owen Talbrook – Speaker Flyer</title>
<link href="https://fonts.googleapis.com/css2?family=Fira+Sans+Condensed:wght@400;500&family=Fira+Sans+Extra+Condensed:wght@700&display=swap" rel="stylesheet">
<style>
  :root {
    --navy: #1d3f72;
    --aqua: #1fa7dc;
    --aqua-deep: #0d7fb8;
    --grey-text: #6d6f73;
    --text-dark: #2a2a2a;
  }
  * { margin: 0; padding: 0; box-sizing: border-box; }
  html, body { width: 848px; height: 1200px; overflow: hidden; background: #fff; }
  .flyer {
    position: relative;
    width: 848px;
    height: 1200px;
    background: #fff;
    font-family: "Fira Sans Condensed", sans-serif;
  }
  .lead-in {
    position: absolute;
    top: 112px;
    left: 0;
    width: 100%;
    text-align: center;
    font-size: 30px;
    font-weight: 400;
    color: var(--navy);
  }
  .topics {
    position: absolute;
    top: 0;
    left: 0;
    width: 100%;
    font-family: "Fira Sans Extra Condensed", sans-serif;
    font-weight: 700;
    font-size: 63px;
    line-height: 1;
    color: var(--aqua);
    text-shadow: 1px 2px 0 var(--aqua-deep), 2px 4px 5px rgba(0,0,0,0.25);
  }
  .topics span { position: absolute; white-space: nowrap; }
  .topic-health { top: 180px; left: 78px; }
  .topic-motivation { top: 248px; left: 182px; }
  .topic-balance { top: 315px; left: 345px; }

  .photo-band {
    position: absolute;
    top: 410px;
    left: 0;
    width: 848px;
    height: 560px;
  }
  .portrait {
    position: absolute;
    top: 422px;
    left: 79px;
    width: 380px;
    height: 536px;
    background:
      radial-gradient(ellipse 90px 110px at 165px 120px, #e2c2ad 0%, rgba(226,194,173,0) 100%),
      linear-gradient(180deg, #9a7f6c 0%, #8f7868 28%, #b9c3d3 55%, #cdd5e2 80%, #b7a497 100%);
    box-shadow: 0 2px 8px rgba(0,0,0,0.3);
  }
  .endorsement {
    position: absolute;
    top: 992px;
    left: 0;
    width: 100%;
    text-align: center;
    font-size: 20px;
    color: var(--text-dark);
  }
  .brand {
    position: absolute;
    top: 1088px;
    left: 0;
    width: 100%;
    text-align: center;
    font-size: 32px;
    font-weight: 400;
    letter-spacing: 2px;
    color: var(--aqua-deep);
    line-height: 1;
  }
  .brand-tagline {
    position: absolute;
    top: 1128px;
    left: 0;
    width: 100%;
    text-align: center;
    font-size: 12px;
    letter-spacing: 1px;
    color: var(--grey-text);
    text-transform: uppercase;
  }
</style>
</head>
<body>
<div class="flyer">
  <p class="lead-in">Looking for an entertaining, high motivation speaker on</p>

  <h1 class="topics">
    <span class="topic-health">health &amp; wellbeing …</span>
    <span class="topic-motivation">motivation …</span>
    <span class="topic-balance">work-life balance?</span>
  </h1>

  <svg class="photo-band" viewBox="0 0 848 560">
    <defs>
      <linearGradient id="bandFade" x1="0" y1="0" x2="0" y2="1">
        <stop offset="0" stop-color="#ffffff"/>
        <stop offset="0.5" stop-color="#dcdde0"/>
        <stop offset="1" stop-color="#ffffff"/>
      </linearGradient>
      <radialGradient id="crowdTone" cx="0.62" cy="0.62" r="0.75">
        <stop offset="0" stop-color="#b68a72"/>
        <stop offset="0.45" stop-color="#8a5a50"/>
        <stop offset="0.8" stop-color="#5a3c44"/>
        <stop offset="1" stop-color="#3e2f3a"/>
      </radialGradient>
    </defs>
    <rect x="0" y="0" width="848" height="560" fill="url(#bandFade)"/>
    <path d="M0 72 Q424 70 848 56 L848 504 Q424 512 0 514 Z" fill="url(#crowdTone)" role="img" aria-label="Photo of a large conference audience raising their hands and cheering"/>
    <path d="M0 62 Q300 70 848 24" fill="none" stroke="#1fa7dc" stroke-width="3"/>
    <path d="M0 54 Q350 60 848 10" fill="none" stroke="#0d7fb8" stroke-width="1.5"/>
    <path d="M450 66 Q650 56 848 42" fill="none" stroke="#ffffff" stroke-width="2"/>
    <path d="M0 524 Q420 496 848 512" fill="none" stroke="#1fa7dc" stroke-width="3"/>
    <path d="M0 534 Q430 506 848 530" fill="none" stroke="#0d7fb8" stroke-width="1.5"/>
    <path d="M450 506 Q650 500 848 508" fill="none" stroke="#ffffff" stroke-width="2"/>
  </svg>

  <div class="portrait" role="img" aria-label="Photo of the speaker on stage in a light blue shirt holding a lit sparkler"></div>

  <p class="endorsement">“… inspirational” – Coastal Meridian Bank</p>

  <p class="brand">OWEN TALBROOK</p>
  <p class="brand-tagline">Health Wellbeing Work-Life Balance</p>
</div>
</body>
</html>
```